Business card for a vending machine business

I need a business card for my vending machine business. The name is Kestrel Snackworks, LLC. The card is one-sided, and landscape format. Not portrait.

The information for the card is as follows:

Dana Whitlow
Owner
(555) 314-2907
Kestrelsnackworks.example
Info@kestrelsnackworks.example

I'd like colors and design elements to match what's in my logo and company name. I'd like to have the checkered flag or racing stripe if possible You can use a border if youd like. You can use a background color if it looks nice and doesn't clash with the logo
Use your creativity. But a white background is perfectly fine. The card can be as simple, yet gets the point across to match the company name and logo.

I uploaded a copy of my logo. I also uploaded a businesses card I started to create, but since it was missing something, I gave up. Another upload has a red thunderbolt and the checkerer flag. Those two uploads are for inspiration. Again, please make sure to make the card landscape, not portrait. Thank you, designers. Good luck to all.

```html
<!DOCTYPE html>
<html lang="en">
<head>
<meta charset="utf-8">
<title>Kestrel Snackworks – Business Card</title>
<link href="https://fonts.googleapis.com/css2?family=Open+Sans:wght@400;600;700&display=swap" rel="stylesheet">
<style>
  :root {
    --page-bg: #a8a9ad;
    --card-bg: #061615;
    --brand-red: #e8383b;
    --text-light: #ffffff;
    --mascot-blue: #2a7fb8;
    --mascot-grey: #cfd6dc;
    --band-light: #f2f2f2;
    --band-dark: #1a1a1a;
  }
  * { margin: 0; padding: 0; box-sizing: border-box; }
  html, body {
    width: 1200px; height: 1131px; overflow: hidden;
    background: var(--page-bg);
    font-family: "Open Sans", Arial, sans-serif;
  }
  .card {
    position: absolute; left: 72px; top: 261px;
    width: 1055px; height: 609px;
    background: var(--card-bg);
    overflow: hidden;
  }
  .logo-art {
    position: absolute; left: 408px; top: 62px;
    width: 195px; height: 176px;
    border-radius: 14px;
    background: linear-gradient(135deg, var(--mascot-grey) 0%, var(--mascot-blue) 70%, var(--brand-red) 100%);
    opacity: .85;
  }
  .brand-name {
    position: absolute; left: 0; width: 100%; top: 250px;
    text-align: center;
    font-weight: 700; font-size: 42px; color: var(--brand-red);
  }
  .identity {
    position: absolute; right: calc(1055px - 501px); top: 398px;
    text-align: right;
  }
  .identity .person {
    font-weight: 600; font-size: 50px; line-height: 60px;
    color: var(--brand-red); text-transform: uppercase; white-space: nowrap;
  }
  .identity .role {
    font-size: 29px; line-height: 36px; color: var(--text-light);
  }
  .divider {
    position: absolute; left: 527px; top: 364px;
    width: 3px; height: 162px; background: var(--text-light);
  }
  .contact {
    position: absolute; left: 558px; top: 372px; list-style: none;
  }
  .contact li {
    display: flex; align-items: center; height: 50px;
    font-size: 29px; color: var(--text-light); white-space: nowrap;
  }
  .contact svg { width: 27px; height: 27px; margin-right: 12px; fill: var(--brand-red); flex: none; }
  .contact .phone { letter-spacing: 4px; }
  .flag-band {
    position: absolute; left: 0; bottom: 0; width: 100%; height: 56px;
    background: linear-gradient(90deg, var(--band-light), #9a9a9a 50%, var(--band-light));
    border-top: 2px solid var(--band-dark);
  }
</style>
</head>
<body>
  <div class="card">
    <div class="logo-art" role="img" aria-label="Mascot illustration: smiling vending machine waving a racing flag"></div>
    <div class="brand-name">Kestrel Snackworks</div>

    <div class="identity">
      <div class="person">Dana Whitlow</div>
      <div class="role">Owner</div>
    </div>

    <div class="divider"></div>

    <ul class="contact">
      <li class="phone">
        <svg viewBox="0 0 24 24"><path d="M6.6 10.8c1.4 2.8 3.8 5.1 6.6 6.6l2.2-2.2c.3-.3.7-.4 1-.2 1.1.4 2.3.6 3.6.6.6 0 1 .4 1 1V20c0 .6-.4 1-1 1C10.6 21 3 13.4 3 4c0-.6.4-1 1-1h3.5c.6 0 1 .4 1 1 0 1.3.2 2.5.6 3.6.1.3 0 .7-.2 1L6.6 10.8z"/></svg>
        (555) 314-2907
      </li>
      <li>
        <svg viewBox="0 0 24 24"><path d="M2 5h20v14H2z" fill="none"/><path d="M2 5h20v2l-10 6L2 7z"/><path d="M2 9l7 4.5L2 18zM22 9l-7 4.5 7 4.5zM10.5 14.5 12 15.5l1.5-1L21 19H3z"/></svg>
        Info@kestrelsnackworks.example
      </li>
      <li>
        <svg viewBox="0 0 24 24"><path d="M12 2a10 10 0 1 0 0 20 10 10 0 0 0 0-20zm6.9 6h-2.9a15 15 0 0 0-1.4-3.6A8 8 0 0 1 18.9 8zM12 4c.8 1.1 1.5 2.5 1.9 4h-3.8c.4-1.5 1.1-2.9 1.9-4zM4.3 14a8 8 0 0 1 0-4h3.4a16 16 0 0 0 0 4zm.8 2h2.9c.3 1.3.8 2.5 1.4 3.6A8 8 0 0 1 5.1 16zM8 8H5.1a8 8 0 0 1 4.3-3.6C8.8 5.5 8.3 6.7 8 8zm4 12c-.8-1.1-1.5-2.5-1.9-4h3.8c-.4 1.5-1.1 2.9-1.9 4zm2.3-6H9.7a14 14 0 0 1 0-4h4.6a14 14 0 0 1 0 4zm.3 5.6c.6-1.1 1.1-2.3 1.4-3.6h2.9a8 8 0 0 1-4.3 3.6zm1.7-5.6a16 16 0 0 0 0-4h3.4a8 8 0 0 1 0 4z"/></svg>
        Kestrelsnackworks.example
      </li>
    </ul>

    <div class="flag-band" role="img" aria-label="Black and white checkered racing flag band"></div>
  </div>
</body>
</html>
```